Law firm needs business card and letter head designed

I need a business card and a letter head for a law firm, well its not really a law firm as it is just me.
The letter head is to have the logo located on the top right hand side, with a footer designed as well. The footer will also be on the second page but the main logo design will not be on the second page.

The business card is to be doubled sided.

The business name is Bramwell Legal.

Industry/Entity Type

Legal

Requirements
Must have
• The letterhead is to have the logo top right hand side of the front page with email address tcorrigan@bramwelllegal.com.au and phone number 0432 817 265, with a footer designed that incorporates the logo, the footer is also to include the following wording Liability Limited by a scheme approved under Professional Standards Legislation.
• I would like the letterhead design to have a second page, with this page just having the footer design, the second page does not need to have the wording above.
• The business card is to be double sides, with one side having my name Tobias Corrigan and title Principal, along with the number 0432 817 265 and the email tcorrigan@bramwelllegal.com.au
• I would like a classy design but with some edge.

```html
<!DOCTYPE html>
<html lang="en">
<head>
<meta charset="utf-8">
<title>Bramwell Legal – Business Card</title>
<link href="https://fonts.googleapis.com/css2?family=Source+Sans+3:wght@400;600&display=swap" rel="stylesheet">
<style>
  :root {
    --backdrop: #000000;
    --card: #323235;
    --brand-blue: #1f7194;
    --text-light: #f2f2f2;
    --divider: #45454a;
  }
  * { margin: 0; padding: 0; box-sizing: border-box; }
  html, body {
    width: 1200px;
    height: 900px;
    overflow: hidden;
    background: var(--backdrop);
    font-family: "Source Sans 3", "Myriad Pro", Arial, sans-serif;
  }
  .stage { position: relative; width: 1200px; height: 900px; }

  .card {
    position: absolute;
    top: 271px;
    width: 457px;
    height: 281px;
    background: var(--card);
    border-radius: 14px;
  }
  .card--contact { left: 137px; }
  .card--brand { left: 626px; }

  .brand-name {
    position: absolute;
    color: var(--brand-blue);
    font-weight: 600;
    text-transform: uppercase;
    white-space: nowrap;
    transform: translateX(-50%);
  }
  .card--contact .brand-name {
    left: 112px;
    top: 128px;
    font-size: 17px;
    letter-spacing: 1px;
  }
  .card--brand .brand-name {
    left: 229px;
    top: 182px;
    font-size: 27px;
    letter-spacing: 0.5px;
  }

  .divider {
    position: absolute;
    left: 216px;
    top: 84px;
    width: 1px;
    height: 116px;
    background: var(--divider);
  }

  .holder {
    position: absolute;
    left: 241px;
    top: 93px;
  }
  .holder__name {
    color: var(--brand-blue);
    font-size: 17px;
    font-weight: 600;
    line-height: 20px;
  }
  .holder__title {
    color: var(--text-light);
    font-size: 13px;
    line-height: 18px;
    margin-top: 1px;
  }

  .contact-list {
    position: absolute;
    left: 241px;
    top: 155px;
    list-style: none;
  }
  .contact-list li {
    display: flex;
    align-items: center;
    gap: 7px;
    color: var(--text-light);
    font-size: 13px;
    line-height: 19px;
  }
  .contact-list svg { width: 9px; height: 9px; fill: var(--brand-blue); flex: none; }
</style>
</head>
<body>
<main class="stage">
  <section class="card card--contact">
    <span class="brand-name">Bramwell Legal</span>
    <span class="divider"></span>
    <div class="holder">
      <p class="holder__name">Tobias Corrigan</p>
      <p class="holder__title">Principal</p>
    </div>
    <ul class="contact-list">
      <li>
        <svg viewBox="0 0 24 24" aria-hidden="true"><path d="M6.6 10.8a15.2 15.2 0 0 0 6.6 6.6l2.2-2.2c.3-.3.7-.4 1-.2 1.1.4 2.3.6 3.6.6.6 0 1 .4 1 1V20c0 .6-.4 1-1 1A17 17 0 0 1 3 4c0-.6.4-1 1-1h3.5c.6 0 1 .4 1 1 0 1.3.2 2.5.6 3.6.1.3 0 .7-.2 1z"/></svg>
        0432 817 265
      </li>
      <li>
        <svg viewBox="0 0 24 24" aria-hidden="true"><path d="M2 5h20v14H2zm2 2v.4l8 5 8-5V7l-8 5z"/></svg>
        tcorrigan@bramwelllegal.com.au
      </li>
    </ul>
  </section>

  <section class="card card--brand">
    <span class="brand-name">Bramwell Legal</span>
  </section>
</main>
</body>
</html>
```